Fall for Display rack for Fall Plant program to be displayed in Yard Vault

Signage for retail plant promotion for fall. Should picture a front porch with fall plants and have our logo on the bottom and the yard vault logo. Could feature fall items like pumkins, cinnamon, gords and more. Should have promotional tital Fresh for Fall! Should have the following selling components as well - Natural Front Door Decor / Enjoy Warm & Cozy Color/ Generate Fall Fresh Air. All should look festive, fresh and have a white wood background. Sign will measure 3 to 4 foot tall by 22.2inches
Target Market(s)
Mass Market Retail - Garden
Industry/Entity Type
Home And Garden
Requirements
Nice to have
- Fall colors. Doesnt have to be exactly what was picked just needs to look like fall.

```html
<!DOCTYPE html>
<html lang="en">
<head>
<meta charset="utf-8">
<title>Fresh for Fall – Verdant Hollow</title>
<link href="https://fonts.googleapis.com/css2?family=Montserrat:wght@500;700;800&display=swap" rel="stylesheet">
<style>
  :root {
    --wood-base: #f1efec;
    --wood-grain: rgba(160, 150, 140, 0.16);
    --plank-seam: rgba(150, 140, 130, 0.22);
    --sketch-tone: rgba(205, 190, 175, 0.35);
    --brand-green: #3f5a2c;
    --ring-green: #8dc63f;
    --promo-red: #ef4b50;
    --leaf-pink: #e23a72;
    --leaf-plum: #5e2433;
    --leaf-mauve: #7c5a6e;
    --text-dark: #333333;
    --white: #ffffff;
    --divider: #6f6f6f;
  }
  * { box-sizing: border-box; margin: 0; padding: 0; }
  html, body { width: 900px; height: 1200px; overflow: hidden; background: #ffffff; }
  .poster {
    position: relative;
    width: 900px;
    height: 1200px;
    font-family: "Montserrat", sans-serif;
    overflow: hidden;
    background: var(--wood-base);
  }
  .wood-background {
    position: absolute;
    inset: 0;
    background:
      repeating-linear-gradient(180deg, transparent 0 149px, var(--plank-seam) 149px 151px),
      repeating-linear-gradient(180deg, transparent 0 9px, var(--wood-grain) 9px 10px, transparent 10px 23px, var(--wood-grain) 23px 24px),
      linear-gradient(90deg, #f6f5f3 0%, #ebe9e6 50%, #f6f5f3 100%);
  }
  .spice-sketches {
    position: absolute;
    inset: 0;
    background:
      radial-gradient(ellipse 160px 220px at 90px 380px, var(--sketch-tone), transparent 70%),
      radial-gradient(ellipse 150px 200px at 820px 300px, var(--sketch-tone), transparent 70%),
      radial-gradient(ellipse 170px 230px at 830px 900px, var(--sketch-tone), transparent 70%),
      radial-gradient(ellipse 170px 200px at 90px 960px, var(--sketch-tone), transparent 70%),
      radial-gradient(ellipse 220px 90px at 300px 20px, var(--sketch-tone), transparent 70%);
  }
  .brand {
    position: absolute;
    top: 76px;
    left: 0;
    right: 0;
    display: flex;
    justify-content: center;
    align-items: center;
    gap: 24px;
  }
  .brand-square {
    width: 96px;
    height: 88px;
    background: var(--brand-green);
  }
  .brand-name {
    display: flex;
    flex-direction: column;
    color: var(--brand-green);
    font-weight: 500;
    text-transform: uppercase;
    line-height: 1;
  }
  .brand-name-main { font-size: 70px; letter-spacing: 0; }
  .brand-name-sub { font-size: 22px; letter-spacing: 23px; margin-top: 6px; }
  .leaf-burst {
    position: absolute;
    left: 450px;
    top: 575px;
    width: 860px;
    height: 760px;
    margin: -380px 0 0 -430px;
    border-radius: 50%;
    background:
      radial-gradient(ellipse at center,
        var(--leaf-plum) 0%,
        var(--leaf-plum) 34%,
        var(--leaf-pink) 46%,
        var(--leaf-mauve) 56%,
        rgba(226, 58, 114, 0.55) 64%,
        rgba(241, 239, 236, 0) 71%);
  }
  .promo-badge {
    position: absolute;
    left: 450px;
    top: 570px;
    width: 490px;
    height: 490px;
    margin: -245px 0 0 -245px;
    border-radius: 50%;
    border: 7px solid var(--ring-green);
    display: flex;
    align-items: center;
    justify-content: center;
  }
  .promo-disc {
    width: 452px;
    height: 452px;
    border-radius: 50%;
    background: var(--promo-red);
    display: flex;
    flex-direction: column;
    align-items: center;
    justify-content: center;
    color: var(--white);
    text-align: center;
    padding-top: 10px;
  }
  .promo-title {
    font-weight: 800;
    font-size: 74px;
    line-height: 0.98;
    text-transform: uppercase;
    letter-spacing: 1px;
  }
  .promo-rule {
    width: 276px;
    height: 2px;
    background: var(--white);
    margin: 22px 0 14px;
  }
  .promo-url {
    font-weight: 700;
    font-size: 18px;
  }
  .benefits {
    position: absolute;
    left: 30px;
    right: 30px;
    top: 990px;
    display: flex;
    justify-content: space-between;
  }
  .benefit {
    flex: 1;
    display: flex;
    flex-direction: column;
    align-items: center;
    gap: 12px;
    padding-top: 6px;
  }
  .benefit-divider {
    width: 0;
    border-left: 2px dashed var(--divider);
    height: 134px;
  }
  .benefit-icon { width: 76px; height: 76px; }
  .benefit-label {
    font-weight: 700;
    font-size: 25px;
    line-height: 1.2;
    color: var(--text-dark);
    text-align: center;
  }
</style>
</head>
<body>
<main class="poster">
  <div class="wood-background"></div>
  <div class="spice-sketches" role="img" aria-label="Faint line sketches of cinnamon sticks, star anise, cloves and fall herbs over white-washed wood"></div>

  <header class="brand">
    <span class="brand-square"></span>
    <span class="brand-name">
      <span class="brand-name-main">Verdant</span>
      <span class="brand-name-sub">Hollow</span>
    </span>
  </header>

  <div class="leaf-burst" role="img" aria-label="Sunburst of pink, burgundy and mauve ti plant leaves radiating around the title"></div>

  <section class="promo-badge">
    <div class="promo-disc">
      <h1 class="promo-title">Fresh<br>for<br>Fall!</h1>
      <div class="promo-rule"></div>
      <p class="promo-url">www.verdanthollow.com</p>
    </div>
  </section>

  <section class="benefits">
    <div class="benefit">
      <svg class="benefit-icon" viewBox="0 0 80 80" aria-hidden="true">
        <circle cx="36" cy="40" r="34" fill="var(--ring-green)"/>
        <circle cx="42" cy="40" r="34" fill="var(--promo-red)"/>
        <path d="M30 60 V32 a12 12 0 0 1 24 0 V60 Z" fill="none" stroke="#fff" stroke-width="3"/>
        <line x1="36" y1="36" x2="36" y2="54" stroke="#fff" stroke-width="2"/>
        <line x1="42" y1="30" x2="42" y2="54" stroke="#fff" stroke-width="2"/>
        <line x1="48" y1="36" x2="48" y2="54" stroke="#fff" stroke-width="2"/>
      </svg>
      <p class="benefit-label">Natural Front<br>Door Decor</p>
    </div>
    <div class="benefit-divider"></div>
    <div class="benefit">
      <svg class="benefit-icon" viewBox="0 0 80 80" aria-hidden="true">
        <circle cx="36" cy="40" r="34" fill="var(--ring-green)"/>
        <circle cx="42" cy="40" r="34" fill="var(--promo-red)"/>
        <circle cx="42" cy="40" r="9" fill="none" stroke="#fff" stroke-width="3"/>
        <g stroke="#fff" stroke-width="3" stroke-linecap="round">
          <line x1="42" y1="20" x2="42" y2="25"/><line x1="42" y1="55" x2="42" y2="60"/>
          <line x1="22" y1="40" x2="27" y2="40"/><line x1="57" y1="40" x2="62" y2="40"/>
          <line x1="28" y1="26" x2="31" y2="29"/><line x1="53" y1="51" x2="56" y2="54"/>
          <line x1="56" y1="26" x2="53" y2="29"/><line x1="31" y1="51" x2="28" y2="54"/>
        </g>
      </svg>
      <p class="benefit-label">Enjoy Warm &amp;<br>Cozy Color</p>
    </div>
    <div class="benefit-divider"></div>
    <div class="benefit">
      <svg class="benefit-icon" viewBox="0 0 80 80" aria-hidden="true">
        <circle cx="36" cy="40" r="34" fill="var(--ring-green)"/>
        <circle cx="42" cy="40" r="34" fill="var(--promo-red)"/>
        <g fill="none" stroke="#fff" stroke-width="3" stroke-linecap="round">
          <path d="M26 32 H50 a5 5 0 1 0 -5 -5"/>
          <path d="M26 40 H56"/>
          <path d="M26 48 H48 a5 5 0 1 1 -5 5"/>
        </g>
      </svg>
      <p class="benefit-label">Generate Fall<br>Fresh Air</p>
    </div>
  </section>
</main>
</body>
</html>
```